Business Cards Needed for Innovative Healthcare Marketing Company

We are a marketing company focused on healthcare. Our company is all about rebranding yourself renewing your image and generating results. The phoenix stands for "reborn" or "rising" which we provide new brands for our clients we take their old brands and renew it with creativity and innovation. I am looking for a business card with color dimension. I have attached an example of a card I think has the look and feel of what I am trying to accomplish. I like that the card example has black and grey font colors, I like the font placement and the small logo, I really like the use of the colors on the right those are the colors of my logo. My logo is phoenix so maybe incorporating flames similar to that design. I would like the back a solid color maybe red with an opaque version of the logo and website. As a marketing company I am always open to creative liberty!

Target Market(s)

Doctors and business professionals.

Industry/Entity Type

Marketing

Contact Information for Business Card

Vornaly Health Care Marketing
Marnie Okonski- CEO
#(502)638-2947
email-marnie@vornaly.com
website- vornaly.com

Font styles to use
Sans Serif

Colors
ec1f27
f37122
ffc214
fbed22
fbf289
f04a50

Requirements
Must have
• The logo and required information
Nice to have
• icons by the information
Should not have
• child like font

```html
<!DOCTYPE html>
<html lang="en">
<head>
<meta charset="utf-8">
<title>Vornaly Health Care Marketing – Business Cards</title>
<link rel="stylesheet" href="https://fonts.googleapis.com/css2?family=Josefin+Sans:wght@300&family=Fira+Sans:wght@400;700&display=swap">
<style>
  :root {
    --bg: #121212;
    --card-front: #ea8e26;
    --card-back: #f0efec;
    --brand-red: #a11d22;
    --brand-red-soft: #c04a4e;
    --flame-orange: #f37122;
    --ink: #2f2f2f;
    --rule: #d9a2a4;
  }
  * { box-sizing: border-box; margin: 0; padding: 0; }
  html, body { width: 1200px; height: 1200px; overflow: hidden; }
  body {
    background: var(--bg);
    position: relative;
    font-family: "Fira Sans", sans-serif;
  }
  .card {
    position: absolute;
    width: 700px;
    height: 400px;
    box-shadow: 0 6px 0 #9a9a9a, 0 10px 0 #6f6f6f, 0 14px 30px rgba(0,0,0,.6);
  }
  .card--front { left: 100px; top: 110px; background: var(--card-front); }
  .card--back { left: 400px; top: 660px; background: var(--card-back); }

  .lockup { position: absolute; display: flex; align-items: center; gap: 22px; }
  .card--front .lockup { left: 120px; top: 150px; }
  .card--back .lockup { left: 60px; top: 140px; }
  .lockup__mark {
    width: 78px; height: 78px; border-radius: 50%;
    background: var(--flame-orange);
    flex: none;
  }
  .card--front .lockup__mark { background: #d2561c; }
  .lockup__name {
    font-family: "Josefin Sans", sans-serif;
    font-weight: 300;
    font-size: 58px;
    letter-spacing: 2px;
    color: var(--brand-red);
    line-height: 1;
  }
  .lockup__tagline {
    font-family: "Josefin Sans", sans-serif;
    font-weight: 300;
    font-size: 15px;
    letter-spacing: 1.5px;
    color: var(--brand-red-soft);
    border-top: 1px solid var(--brand-red-soft);
    margin-top: 6px;
    padding-top: 5px;
  }
  .card--front .lockup__tagline { color: #9e2a1d; border-color: #b5502c; }

  .person {
    position: absolute; left: 420px; top: 112px;
    border-left: 1px solid var(--rule);
    padding-left: 16px;
  }
  .person__name { font-weight: 700; font-size: 30px; color: var(--brand-red); }
  .person__role { font-size: 17px; color: var(--ink); margin-top: 2px; }

  .contacts {
    position: absolute; left: 430px; top: 210px;
    border-left: 1px solid var(--rule);
    padding: 4px 0 4px 16px;
    list-style: none;
  }
  .contacts__item {
    display: flex; align-items: center; gap: 10px;
    font-size: 18px; color: var(--ink);
    margin: 7px 0;
  }
  .contacts__item--web { letter-spacing: 3px; }
  .contacts__icon { width: 18px; height: 18px; flex: none; }
</style>
</head>
<body>
  <section class="card card--front" aria-label="Card back">
    <div class="lockup">
      <span class="lockup__mark"></span>
      <div>
        <div class="lockup__name">VORNALY</div>
        <div class="lockup__tagline">HEALTHCARE MARKETING</div>
      </div>
    </div>
  </section>

  <section class="card card--back" aria-label="Card front">
    <div class="lockup">
      <span class="lockup__mark"></span>
      <div>
        <div class="lockup__name" style="font-size:44px">VORNALY</div>
        <div class="lockup__tagline" style="font-size:12px">HEALTHCARE MARKETING</div>
      </div>
    </div>

    <div class="person">
      <div class="person__name">Marnie Okonski</div>
      <div class="person__role">CEO</div>
    </div>

    <ul class="contacts">
      <li class="contacts__item">
        <svg class="contacts__icon" viewBox="0 0 24 24"><path fill="#a11d22" d="M6.6 10.8a15 15 0 0 0 6.6 6.6l2.2-2.2a1 1 0 0 1 1-.25 11.4 11.4 0 0 0 3.6.57 1 1 0 0 1 1 1V20a1 1 0 0 1-1 1A17 17 0 0 1 3 4a1 1 0 0 1 1-1h3.5a1 1 0 0 1 1 1c0 1.25.2 2.45.57 3.57a1 1 0 0 1-.25 1z"/></svg>
        (502)638-2947
      </li>
      <li class="contacts__item contacts__item--web">
        <svg class="contacts__icon" viewBox="0 0 24 24" fill="none" stroke="#a11d22" stroke-width="2"><circle cx="12" cy="12" r="9"/><path d="M3 12h18M12 3c3 3.5 3 14.5 0 18M12 3c-3 3.5-3 14.5 0 18"/></svg>
        vornaly.com
      </li>
      <li class="contacts__item">
        <svg class="contacts__icon" viewBox="0 0 24 24"><rect x="2" y="5" width="20" height="14" rx="2" fill="#a11d22"/><path d="M3 6l9 7 9-7" fill="none" stroke="#f0efec" stroke-width="1.6"/></svg>
        marnie@vornaly.com
      </li>
    </ul>
  </section>
</body>
</html>
```